Email Signature

We are looking for creative email signature for our company. Please find attached the logo of our company for your reference. now we understand there isn't much can be done with email signature but we are looking for out of the box designs. Nothing specific in mind

Please insert fake numbers, website and/or address, etc just to showcase the designs. once the design is chosen we will provide the actual details.
Updates

Dear All,

We wouldlike to extend our apology for not being able to provide feedbacks to everysingle design. We were extremely busy and we have multiple contests opensimultaneously which makes the process harder. However, thank you all for theefforts you have put into this contest. We have received anoverwhelming quality responses & it has been a very difficult task tochoose just one, we easily Loved at least several designs...

Thanksagain for participating, we wish you all success in your design ventures.

Kindregards,

HLW Team

Industry/Entity Type

It Company

```html
<!DOCTYPE html>
<html lang="en">
<head>
<meta charset="utf-8">
<title>ParcelNest Email Signature</title>
<link rel="stylesheet" href="https://fonts.googleapis.com/css2?family=Arimo:wght@400;700&display=swap">
<style>
  :root {
    --ink: #1a1a1a;
    --brand-blue: #1f78d1;
    --contact-blue: #1668c4;
    --brand-green: #6bbf3a;
    --paper: #ffffff;
  }
  * { margin: 0; padding: 0; box-sizing: border-box; }
  html, body { width: 1200px; height: 419px; overflow: hidden; background: var(--paper); }
  body { font-family: "Arimo", Arial, sans-serif; color: var(--ink); position: relative; }

  .sign-off { position: absolute; left: 86px; top: 32px; font-size: 19px; line-height: 29px; }
  .sign-off .name, .sign-off .role, .sign-off .dots { font-weight: 700; }

  .brand { position: absolute; left: 80px; top: 152px; display: flex; align-items: center; gap: 14px; }
  .brand-name { font-size: 78px; font-weight: 700; color: var(--brand-blue); letter-spacing: -1px; line-height: 1; }
  .brand-dot { width: 30px; height: 30px; border-radius: 50%; background: var(--brand-green); margin-top: 30px; }

  .address { position: absolute; left: 80px; top: 236px; font-size: 19px; line-height: 24px; color: var(--ink); }

  .contacts { position: absolute; left: 84px; top: 286px; width: 1064px; height: 86px; display: flex; }
  .contact { position: relative; display: flex; flex-direction: column; align-items: center; justify-content: space-between; padding: 6px 8px 10px 19px; }
  .contact.phone-main { width: 223px; }
  .contact.phone-alt { width: 260px; }
  .contact.email { width: 307px; }
  .contact.web { width: 263px; }
  .bar { position: absolute; top: 0; width: 11px; height: 86px; }
  .bar::before, .bar::after { content: ""; position: absolute; top: 0; height: 100%; background: var(--contact-blue); }
  .bar::before { left: 0; width: 5px; }
  .bar::after { left: 8px; width: 3px; }
  .contact .bar { left: 0; }
  .contact .bar.end { right: -11px; left: auto; }
  .icon { width: 30px; height: 30px; }
  .value { font-size: 25px; color: var(--contact-blue); white-space: nowrap; }
</style>
</head>
<body>
  <div class="sign-off">
    <div class="greeting">Best Wishes</div>
    <div class="name">Dana Whitfield</div>
    <div class="role">Marketing Manager</div>
    <div class="dots">...</div>
  </div>

  <div class="brand">
    <span class="brand-name">ParcelNest</span>
    <span class="brand-dot"></span>
  </div>

  <div class="address">
    <div>7465 Address Information Address</div>
    <div>Information Address Information</div>
  </div>

  <div class="contacts">
    <div class="contact phone-main">
      <span class="bar"></span>
      <svg class="icon" viewBox="0 0 30 30" aria-hidden="true">
        <circle cx="15" cy="15" r="15" fill="var(--brand-green)"/>
        <path d="M10 8c1-1 2-1 2.5 0l1.5 3c.4.8 0 1.4-.6 1.9l-.8.6c.8 1.8 2.1 3.1 3.9 3.9l.6-.8c.5-.6 1.1-1 1.9-.6l3 1.5c1 .5 1 1.5 0 2.5-1.5 1.5-3.5 1.8-6 .3-2.7-1.6-4.7-3.6-6.3-6.3-1.5-2.5-1.2-4.5.3-6z" fill="#fff"/>
      </svg>
      <span class="value">555-0142-7788</span>
    </div>
    <div class="contact phone-alt">
      <span class="bar"></span>
      <svg class="icon" viewBox="0 0 30 30" aria-hidden="true">
        <circle cx="15" cy="15" r="15" fill="var(--brand-green)"/>
        <rect x="10" y="7" width="10" height="6" fill="#fff"/>
        <rect x="7" y="12" width="16" height="8" rx="1.5" fill="#fff"/>
        <rect x="10" y="17" width="10" height="6" fill="#fff" stroke="var(--brand-green)" stroke-width="1.2"/>
      </svg>
      <span class="value">555-214-0963</span>
    </div>
    <div class="contact email">
      <span class="bar"></span>
      <svg class="icon" viewBox="0 0 30 30" aria-hidden="true">
        <circle cx="15" cy="15" r="15" fill="var(--brand-green)"/>
        <rect x="7.5" y="9.5" width="15" height="11" fill="none" stroke="#fff" stroke-width="1.8"/>
        <path d="M7.5 9.5l7.5 6 7.5-6" fill="none" stroke="#fff" stroke-width="1.8"/>
      </svg>
      <span class="value">hello@parcelnest.com</span>
    </div>
    <div class="contact web">
      <span class="bar"></span>
      <span class="bar end"></span>
      <svg class="icon" viewBox="0 0 30 30" aria-hidden="true">
        <circle cx="15" cy="15" r="15" fill="var(--brand-green)"/>
        <g fill="none" stroke="#fff" stroke-width="1.6">
          <circle cx="15" cy="15" r="7.5"/>
          <ellipse cx="15" cy="15" rx="3.2" ry="7.5"/>
          <path d="M7.5 15h15M9 11h12M9 19h12"/>
        </g>
      </svg>
      <span class="value">www.parcelnest.com</span>
    </div>
  </div>
</body>
</html>
```